HUSH: Hush Until Stories Happen school library event

I need two poster designs for Hush Until Stories Happen (HUSH) in BC, requested by the PCSMG--Pacific Coast School Media Guild. One should be for elementary students and one for high school. I want the date (Monday, October 26, 2020) and Hush Until Stories Happen. I would like the posters in English and in French. French is : Ferme Ton Écran Maintenant! I'm including last year's posters as examples. I would like to be able to print the poster files on 11x17 paper.

• -The phrase "Hush Until Stories Happen" for the English version; "Ferme Ton Écran Maintenant" for the French version.
-Include the organization name: Pacific Coast School Media Guild
-The date: Monday, October 26, 2020
• I would like the elementary version to be bright and colourful--fun for younger kids. I would like the high school version to be a bit more mature for the older students. Can still be bright and colourful.

```html
<!DOCTYPE html>
<html lang="en">
<head>
<meta charset="utf-8">
<title>Hush Until Stories Happen — Monday, October 26, 2020</title>
<link rel="stylesheet" href="https://fonts.googleapis.com/css2?family=Barlow+Condensed:wght@500;800&display=swap">
<style>
  :root {
    --poster-yellow: #fde000;
    --ink: #000000;
  }
  html, body {
    margin: 0;
    padding: 0;
    width: 776px;
    height: 1200px;
    overflow: hidden;
    background: var(--poster-yellow);
  }
  .poster {
    position: relative;
    width: 776px;
    height: 1200px;
    background: var(--poster-yellow);
    overflow: hidden;
  }
  .poster-art {
    position: absolute;
    inset: 0;
    width: 776px;
    height: 1200px;
    display: block;
  }
  .rule { fill: var(--ink); }
  .headline {
    font-family: "Barlow Condensed", "Arial Narrow", sans-serif;
    font-weight: 800;
    fill: var(--ink);
  }
  .org-name {
    position: absolute;
    left: 516px;
    top: 96px;
    margin: 0;
    font-family: "Barlow Condensed", "Arial Narrow", sans-serif;
    font-weight: 500;
    font-size: 33px;
    line-height: 37px;
    color: var(--ink);
  }
  .event-date {
    position: absolute;
    left: 303px;
    top: 932px;
    margin: 0;
    font-family: "Barlow Condensed", "Arial Narrow", sans-serif;
    font-weight: 500;
    font-size: 64px;
    line-height: 65px;
    color: var(--ink);
    letter-spacing: -0.5px;
  }
</style>
</head>
<body>
<main class="poster">
  <svg class="poster-art" viewBox="0 0 776 1200" xmlns="http://www.w3.org/2000/svg" aria-label="Hush Until Stories Happen">
    <!-- structural rules -->
    <rect class="rule rule-top" x="478" y="0" width="6" height="211"/>
    <rect class="rule rule-cross" x="156" y="341" width="620" height="34"/>
    <rect class="rule rule-stem" x="242" y="723" width="38" height="477"/>

    <!-- oversized exclamation at the left edge -->
    <text class="headline mark-exclaim" x="-10" y="1055" font-size="790" textLength="200" lengthAdjust="spacingAndGlyphs">!</text>

    <!-- headline words -->
    <text class="headline word-hush" transform="translate(331 695) rotate(-90)" font-size="250" textLength="409" lengthAdjust="spacingAndGlyphs">HUSH</text>
    <text class="headline word-until" x="359" y="539" font-size="177" textLength="330" lengthAdjust="spacingAndGlyphs">UNTIL</text>
    <text class="headline word-stories" x="359" y="694" font-size="177" textLength="330" lengthAdjust="spacingAndGlyphs">STORIES</text>
    <text class="headline word-happen" x="244" y="921" font-size="283" textLength="445" lengthAdjust="spacingAndGlyphs">HAPPEN</text>
  </svg>

  <p class="org-name">Pacific Coast<br>School Media<br>Guild</p>

  <p class="event-date">Monday,<br>October 26, 2020</p>
</main>
</body>
</html>
```